Pivots & Treads .com

This website is simple!!!
Landing page background image should capture the customers attention!!! We will provide a image as a example of what we like. The purpose for this website is to provide customers with a clean easy way to request a quote for industrial casters and wheels by OEM’s as well as maintenance departments worldwide. Please see if you can follow our thought process below.
Customer comes to website, they are invited to Request a Quote by providing us with Manufacturer Name, Manufacturers Part # and quantity needed.
If this is not known the customer will complete will WP conversation format form answering about 10 questions
Or
Look up the part number in one of the 8 to 12 catalogs located in the Flippin Book format on our catalog page, or equal plug in .
When the client request a quote a account page will pop up request The following:
Clients first and last name
Email address
And optional questions
Company name and best contact number.
Once this is complete customer will hit SUBMIT.
The customers request will be in system. A email will be sent to Customer service notifying us the Quote Request has been made.
We will then build a quote for the customer with a good, better and best options. Customers Request a Quote submission may have more than one caster or wheel requested at a time, so website must allow this.
When the customer comes back into website there email address will come up as the account name and request a password be made for them. This will allow them to store quotes in their account for future needs. If quote is older than 30 day the system will trigger a button at the bottom of the quote for resubmit Request for updated quote.
Once customer reviews quote the quote can be Converted to order within the website.
Once Converted the system will send us a email and order will be processed.
We will need a Chat program that will text to CS the questions.
You will need to have high quality graphic design skills on your team.
We have found 2 plugins that would work nicely with our new website Flippin books to showcase our catalogs for customers to research and WPForms conversation forms to complete request for quote form.
Just Ideas:
Very very ghosted caster blueprint in white background but very very ghosted or the icon just idea
We have never had a font used we like
Grayscale every except for rubber on wheels and logo icon
Website should have hamburger menu on left
Website should hav responsive deign
Account head on right side
Has anyone read the brief from top to bottom and the updates, I’m seeing a lot of duplicates of the website I posted in images I want a clean website With lite backgrand with the poly being definite colors on each wheel I added a green yellow and red image has anyone looked at that Just a question?
Went on vacation/holiday

```html
<!DOCTYPE html>
<html lang="en">
<head>
<meta charset="utf-8">
<title>Pivots &amp; Treads .com</title>
<link rel="stylesheet" href="https://fonts.googleapis.com/css2?family=Montserrat:wght@400;500;600;700;800&family=Raleway:wght@400;500;600&display=swap">
<style>
:root{
  --brand:#2b4a9f;
  --brand-text:#2c4ea0;
  --ink:#222;
  --dark:#2d2d2d;
  --panel:#ebebeb;
  --light:#f4f4f4;
  --white:#fff;
  --red:#d8232a;
  --navy:#1e2a4e;
  --yellow:#e8b60c;
  --grey-tyre:#8f9397;
}
*{box-sizing:border-box;margin:0;padding:0}
html,body{width:1200px;height:2570px;overflow:hidden}
body{position:relative;background:var(--white);font-family:"Montserrat",sans-serif;color:var(--ink)}
.abs{position:absolute}
.topbar{left:0;top:0;width:1200px;height:30px;background:var(--dark)}
.social{display:flex;gap:7px}
.social span{width:16px;height:16px;border-radius:50%;background:#bbb;display:block}
.topbar .social{position:absolute;left:151px;top:7px}
.topbar .phone{position:absolute;right:192px;top:8px;color:#fff;font-size:11px;font-weight:600;display:flex;align-items:center;gap:10px}
.topbar .account{position:absolute;left:1034px;top:6px}
.header{left:0;top:30px;width:1200px;height:78px;background:var(--light);box-shadow:0 1px 3px rgba(0,0,0,.15);z-index:2}
.logo{display:flex;align-items:center;gap:10px;color:var(--brand);font-weight:800;letter-spacing:1px;line-height:1}
.logo .dot{border-radius:50%;background:var(--brand);flex:none}
.header .logo{position:absolute;left:151px;top:26px;font-size:21px}
.header .logo .dot{width:26px;height:26px}
.nav{position:absolute;left:485px;top:0;display:flex;height:78px}
.nav a{display:flex;align-items:center;padding:0 19px;font-size:13px;font-weight:600;color:var(--ink);text-decoration:none;letter-spacing:.5px}
.nav a.active{background:var(--white)}
.nav a.current{box-shadow:inset 0 -3px 0 var(--brand)}
.btn-quote{position:absolute;left:888px;top:16px;width:163px;height:46px;background:var(--brand);color:#fff;font-size:13px;font-weight:600;display:flex;align-items:center;justify-content:center}
.hero{left:0;top:108px;width:1200px;height:450px;background:linear-gradient(180deg,#d2c8b8 0%,#cfc9c0 45%,#d9d8d6 100%)}
.hero h1{position:absolute;left:151px;top:86px;font-size:28px;line-height:41px;font-weight:600;color:var(--brand-text);letter-spacing:.6px}
.features{position:absolute;left:151px;top:182px;list-style:none}
.features li{display:flex;align-items:center;gap:16px;font-size:18px;font-weight:500;letter-spacing:1px;color:#2a2a2a;height:36px}
.btn-dark{background:var(--dark);color:#fff;font-weight:600;display:flex;align-items:center;justify-content:center;letter-spacing:.8px}
.hero .btn-dark{position:absolute;left:190px;top:312px;width:150px;height:44px;font-size:18px}
.product-art{position:absolute}
.side{left:0;width:255px}
.vert{position:absolute;left:145px;writing-mode:vertical-rl;transform:rotate(180deg);font-weight:800;font-size:76px;letter-spacing:-1px;line-height:1;color:#fff}
.quote-sec{top:558px;height:598px}
.intro{position:absolute;left:288px;font-weight:600;color:#222}
.steps{position:absolute;left:288px;top:865px;list-style:none}
.steps li{display:flex;align-items:center;gap:16px;font-size:18px;font-weight:500;letter-spacing:1px;height:36px}
.form{left:673px;top:615px;width:378px;height:485px;background:var(--panel);box-shadow:0 2px 4px rgba(0,0,0,.2);padding:44px 38px 0}
.form label{display:block;font-size:13px;font-weight:600;letter-spacing:.6px}
.select{background:#fff;border:2px solid #d4d4d4;height:38px;display:flex;align-items:center;justify-content:space-between;padding:0 12px;font-size:13px;font-weight:500;letter-spacing:.6px}
.form .get{height:46px;background:var(--brand);color:#fff;font-size:14px;font-weight:600;letter-spacing:1px;display:flex;align-items:center;justify-content:center}
.form .note{font-size:13px;font-weight:500;white-space:nowrap}
.form .note a{color:var(--brand);text-decoration:none}
.products{left:255px;top:1156px;width:945px;height:546px;background:var(--panel)}
.card{position:absolute;top:1316px;width:237px;height:237px;background:#fff;box-shadow:0 1px 3px rgba(0,0,0,.25)}
.card .product-art{left:24px;top:20px;width:189px;height:197px}
.card-label{position:absolute;top:1563px;width:237px;text-align:center;font-size:17px;font-weight:500;letter-spacing:.6px}
.card-btn{position:absolute;top:1606px;width:122px;height:40px;font-size:14px}
.aboutbox{left:311px;top:1759px;width:375px;height:424px;background:var(--panel);box-shadow:0 1px 3px rgba(0,0,0,.2);padding:34px 30px 0 38px;font-family:"Raleway",sans-serif;font-size:15px;line-height:21px;color:#333}
.aboutbox p{margin-bottom:19px}
.footer{left:0;top:2240px;width:1200px;height:310px;background:var(--panel)}
.fh{position:absolute;top:2294px;font-size:16px;font-weight:500;color:#222}
.fline{position:absolute;top:2319px;height:2px;background:#fff}
.ftext{font-family:"Raleway",sans-serif;font-size:12px;line-height:20px;color:#444}
.contact-row{position:absolute;left:485px;display:flex;gap:20px;font-size:13px;line-height:20px;color:#333}
.contact-row svg{flex:none;margin-top:2px}
.subscribe{left:784px;top:2362px;width:269px;height:31px;display:flex;border:1px solid #bbb;background:#fff}
.subscribe span{flex:1;font-size:12px;padding:8px 16px;color:#666;font-family:"Raleway",sans-serif}
.subscribe b{width:91px;background:var(--brand);color:#fff;font-size:12px;font-weight:600;display:flex;align-items:center;justify-content:center}
.footer-social{left:785px;top:2430px;display:flex;gap:13px}
.footer-social span{width:23px;height:23px;border-radius:50%;background:#666;display:block}
.copy{left:0;top:2550px;width:1200px;height:20px;background:var(--dark);color:#fff;font-size:8px;font-weight:600;display:flex;align-items:center;justify-content:center;gap:8px}
</style>
</head>
<body>

<div class="abs topbar">
  <div class="social"><span></span><span></span><span></span><span></span><span></span></div>
  <div class="phone">
    <svg width="15" height="15" viewBox="0 0 24 24"><path fill="#fff" d="M6.6 10.8a15 15 0 0 0 6.6 6.6l2.2-2.2c.3-.3.7-.4 1-.2 1.1.4 2.3.6 3.6.6.6 0 1 .4 1 1V20c0 .6-.4 1-1 1A17 17 0 0 1 3 4c0-.6.4-1 1-1h3.5c.6 0 1 .4 1 1 0 1.3.2 2.5.6 3.6.1.3 0 .7-.2 1z"/></svg>
    0155 210 4478
  </div>
  <svg class="account" width="18" height="18" viewBox="0 0 24 24"><circle cx="12" cy="12" r="11" fill="#fff"/><circle cx="12" cy="9" r="4" fill="#2d2d2d"/><path d="M5 19c1.5-3 4-4 7-4s5.5 1 7 4" fill="#2d2d2d"/></svg>
</div>

<header class="abs header">
  <div class="logo"><span class="dot"></span>PIVOTS &amp; TREADS .com</div>
  <nav class="nav">
    <a class="active">Home</a>
    <a>Products</a>
    <a class="current">About Us</a>
    <a>Contact Us</a>
  </nav>
  <div class="btn-quote">REQUEST A QUOTE</div>
</header>

<section class="abs hero" role="img" aria-label="Softly blurred warehouse aisle with shelving in warm beige tones">
  <h1>One Stop Solution for All Your<br>Caster Wheel Applications</h1>
  <ul class="features">
    <li><svg width="21" height="21" viewBox="0 0 24 24"><circle cx="12" cy="12" r="11" fill="#2b4a9f"/><path fill="#fff" d="M12 5.5l1.9 4 4.3.5-3.2 2.9.9 4.3L12 15l-3.9 2.2.9-4.3-3.2-2.9 4.3-.5z"/></svg>High Quality Caster Wheels</li>
    <li><svg width="21" height="21" viewBox="0 0 24 24"><circle cx="12" cy="12" r="11" fill="#2b4a9f"/><path fill="#fff" d="M12 5.5l1.9 4 4.3.5-3.2 2.9.9 4.3L12 15l-3.9 2.2.9-4.3-3.2-2.9 4.3-.5z"/></svg>Huge Product Range</li>
    <li><svg width="21" height="21" viewBox="0 0 24 24"><circle cx="12" cy="12" r="11" fill="#2b4a9f"/><path fill="#fff" d="M12 5.5l1.9 4 4.3.5-3.2 2.9.9 4.3L12 15l-3.9 2.2.9-4.3-3.2-2.9 4.3-.5z"/></svg>Reasonable Price</li>
  </ul>
  <div class="btn-dark">Learn More</div>
  <div class="product-art" style="left:528px;top:196px;width:172px;height:200px;background:radial-gradient(ellipse 70% 65% at 50% 58%,rgba(216,35,42,.95) 0%,rgba(200,60,60,.75) 40%,rgba(190,190,195,.5) 65%,rgba(210,205,200,0) 100%)" role="img" aria-label="Swivel caster with red polyurethane wheel"></div>
  <div class="product-art" style="left:716px;top:196px;width:172px;height:200px;background:radial-gradient(ellipse 70% 65% at 50% 58%,rgba(30,42,78,.95) 0%,rgba(60,70,100,.75) 40%,rgba(190,190,195,.5) 65%,rgba(210,205,200,0) 100%)" role="img" aria-label="Swivel caster with navy blue wheel"></div>
  <div class="product-art" style="left:900px;top:210px;width:158px;height:188px;background:radial-gradient(ellipse 62% 60% at 50% 52%,rgba(26,26,26,.95) 0%,rgba(60,60,62,.85) 35%,rgba(143,147,151,.8) 58%,rgba(210,205,200,0) 100%)" role="img" aria-label="Grey rubber wheel with black hub"></div>
</section>

<section class="abs side quote-sec" style="background:var(--panel)"><div class="vert" style="top:72px">GET QUOTE</div></section>
<div class="intro" style="top:676px;font-size:19px;letter-spacing:.4px">Solutions for All Your Applications</div>
<div class="intro" style="top:782px;font-size:21px;font-weight:500;letter-spacing:1.5px">Easy as 1-2-3</div>
<ul class="steps">
  <li><svg width="21" height="21" viewBox="0 0 24 24"><circle cx="12" cy="12" r="11" fill="#2b4a9f"/><path d="M10 7l5 5-5 5" stroke="#fff" stroke-width="2.6" fill="none"/></svg>Request a Quote</li>
  <li><svg width="21" height="21" viewBox="0 0 24 24"><circle cx="12" cy="12" r="11" fill="#2b4a9f"/><path d="M10 7l5 5-5 5" stroke="#fff" stroke-width="2.6" fill="none"/></svg>Receive a Quote</li>
  <li><svg width="21" height="21" viewBox="0 0 24 24"><circle cx="12" cy="12" r="11" fill="#2b4a9f"/><path d="M10 7l5 5-5 5" stroke="#fff" stroke-width="2.6" fill="none"/></svg>Convert a Quote to Order</li>
</ul>

<form class="abs form">
  <label>Manufacturer's Name:</label>
  <div class="select" style="margin-top:12px">Select<svg width="16" height="10" viewBox="0 0 16 10"><path d="M1 1l7 7 7-7" stroke="#222" stroke-width="2.4" fill="none"/></svg></div>
  <label style="margin-top:45px">Manufacturer's Part Number:</label>
  <div class="select" style="margin-top:12px">Select<svg width="16" height="10" viewBox="0 0 16 10"><path d="M1 1l7 7 7-7" stroke="#222" stroke-width="2.4" fill="none"/></svg></div>
  <div style="display:flex;align-items:center;justify-content:space-between;margin-top:46px">
    <label>Quantity:</label>
    <div class="select" style="width:151px;font-size:12px">1<svg width="16" height="10" viewBox="0 0 16 10"><path d="M1 1l7 7 7-7" stroke="#222" stroke-width="2.4" fill="none"/></svg></div>
  </div>
  <div class="get" style="margin-top:45px">GET QUOTE</div>
  <p class="note" style="margin-top:36px">Don't Have Manufacturer Details? <a>Click Here</a></p>
</form>

<section class="abs side" style="top:1156px;height:546px;background:var(--white)"><div class="vert" style="top:48px;color:#ebebeb">PRODUCTS</div></section>
<section class="abs products"></section>
<div class="abs btn-dark" style="left:910px;top:1213px;width:141px;height:47px;font-size:17px;gap:10px">View All <svg width="8" height="12" viewBox="0 0 8 12"><path d="M1 1l5 5-5 5" stroke="#fff" stroke-width="2" fill="none"/></svg></div>

<div class="card" style="left:284px"><div class="product-art" style="background:radial-gradient(ellipse 60% 60% at 45% 58%,rgba(216,35,42,.95) 0%,rgba(220,90,90,.6) 45%,rgba(225,225,228,.5) 70%,rgba(255,255,255,0) 100%)" role="img" aria-label="Swivel caster with red wheel"></div></div>
<div class="card" style="left:549px"><div class="product-art" style="background:radial-gradient(ellipse 60% 60% at 45% 58%,rgba(30,42,78,.95) 0%,rgba(80,90,120,.6) 45%,rgba(225,225,228,.5) 70%,rgba(255,255,255,0) 100%)" role="img" aria-label="Swivel caster with navy wheel"></div></div>
<div class="card" style="left:814px"><div class="product-art" style="background:radial-gradient(ellipse 55% 58% at 50% 50%,rgba(26,26,26,.95) 0%,rgba(60,60,62,.85) 35%,rgba(143,147,151,.75) 60%,rgba(255,255,255,0) 100%)" role="img" aria-label="Grey rubber wheel with black hub"></div></div>
<div class="card-label" style="left:284px">Casters</div>
<div class="card-label" style="left:549px">Casters</div>
<div class="card-label" style="left:814px">Wheels</div>
<div class="btn-dark card-btn" style="left:341px">Learn More</div>
<div class="btn-dark card-btn" style="left:606px">Learn More</div>
<div class="btn-dark card-btn" style="left:871px">Learn More</div>

<section class="abs side" style="top:1702px;height:538px;background:var(--panel)"><div class="vert" style="top:56px">ABOUT US</div></section>
<div class="abs aboutbox">
  <p>Lorem ipsum dolor sit amet, consectetur adipiscing elit, sed do eiusmod tempor incididunt ut labore et dolore magna aliqua Quis ipsum suspendisse ultrices gravida. Risus commodo</p>
  <p>Lorem ipsum dolor sit amet, consectetur adipiscing elit, sed do eiusmod tempor incididunt ut labore et dolore magna aliqua Quis ipsum suspendisse ultrices gravida.</p>
  <p>Lorem ipsum dolor sit amet, consectetur adipiscing elit, sed do eiusmod tempor incididunt ut labore et dolore magna aliqua Quis ipsum suspendisse ultrices gravida. Lorem ipsum dolor sit amet, consectetur adipiscing elit, sed do eiusmod tempor</p>
</div>
<div class="abs logo" style="left:778px;top:1764px;font-size:26px;width:276px;line-height:1.1"><span class="dot" style="width:40px;height:40px"></span><span>PIVOTS &amp;<br>TREADS .com</span></div>
<div class="abs product-art" style="left:740px;top:1850px;width:320px;height:340px;background:radial-gradient(ellipse 55% 55% at 45% 58%,rgba(232,182,12,.95) 0%,rgba(232,190,60,.75) 35%,rgba(201,204,208,.6) 62%,rgba(255,255,255,0) 100%)" role="img" aria-label="Heavy duty swivel caster with yellow wheel and spring brake"></div>

<footer class="abs footer"></footer>
<div class="fh" style="left:151px">ABOUT US</div>
<div class="fline" style="left:151px;width:278px"></div>
<div class="abs logo" style="left:151px;top:2358px;font-size:17px;line-height:1.1"><span class="dot" style="width:30px;height:30px"></span><span>PIVOTS &amp;<br>TREADS .com</span></div>
<p class="abs ftext" style="left:151px;top:2412px;width:240px">Lorem ipsum dolor sit amet, consectetur adipiscing elit, sed do eiusmod tempor incididunt ut labore et dolore magna aliqua. Quis ipsum suspendisse ultrices gravida.</p>

<div class="fh" style="left:485px">CONTACT US</div>
<div class="fline" style="left:485px;width:244px"></div>
<div class="contact-row" style="top:2345px"><svg width="13" height="16" viewBox="0 0 12 16"><path fill="#222" d="M6 0a6 6 0 0 0-6 6c0 4.5 6 10 6 10s6-5.5 6-10a6 6 0 0 0-6-6zm0 8.5a2.5 2.5 0 1 1 0-5 2.5 2.5 0 0 1 0 5z"/></svg><span>218 Millbrook Ave, Dunmore,<br>Ohio, 44102</span></div>
<div class="contact-row" style="top:2414px"><svg width="15" height="11" viewBox="0 0 16 12"><rect width="16" height="12" fill="#222"/><path d="M0 0l8 7 8-7" stroke="#fff" stroke-width="1.4" fill="none"/></svg><span>hello@pivotstreads.example</span></div>
<div class="contact-row" style="top:2467px"><svg width="15" height="15" viewBox="0 0 24 24"><path fill="#222" d="M6.6 10.8a15 15 0 0 0 6.6 6.6l2.2-2.2c.3-.3.7-.4 1-.2 1.1.4 2.3.6 3.6.6.6 0 1 .4 1 1V20c0 .6-.4 1-1 1A17 17 0 0 1 3 4c0-.6.4-1 1-1h3.5c.6 0 1 .4 1 1 0 1.3.2 2.5.6 3.6.1.3 0 .7-.2 1z"/></svg><span style="font-size:12px">0155 210 4478</span></div>

<div class="fh" style="left:784px;line-height:19px">SUBSCRIBE TO OUR<br>NEWSLETTER</div>
<div class="abs subscribe"><span>Enter Your Email</span><b>Subscribe</b></div>
<div class="abs footer-social"><span></span><span></span><span></span><span></span><span></span></div>

<div class="abs copy"><span>Copyright © 2022 Pivots &amp; Treads .com</span>|<span>Terms of Service</span>|<span>Privacy Policy</span></div>

</body>
</html>
```